we do all sorts of cleaning however bookings are limited!
why not chose the right cleaners for you!
pressure cleaning, window cleaning, office, end of lease clean, accommodation, industrial and commercial cleaning and house cleaning

Logo Text

Bright Nest Cleaning Service

```html
<!DOCTYPE html>
<html lang="en">
<head>
<meta charset="UTF-8">
<title>Bright Nest Cleaning Service – Business Card</title>
<link rel="stylesheet" href="https://fonts.googleapis.com/css2?family=Poppins:wght@300;400;500;600&display=swap">
<style>
  :root {
    --page-bg: #e9e7e4;
    --card-light: #f7f9fb;
    --card-frost: #dfe8ef;
    --card-dark: #0b0b0c;
    --card-dark-2: #1d1d1f;
    --brand-blue: #2f86c6;
    --band-blue: #2a85bd;
    --brand-green: #4f9a2c;
    --silver: #cfc7c2;
    --muted: #a9a29b;
  }
  * { margin: 0; padding: 0; box-sizing: border-box; }
  html, body {
    width: 1200px;
    height: 970px;
    overflow: hidden;
    background: var(--page-bg);
    font-family: 'Poppins', sans-serif;
  }
  .canvas {
    position: relative;
    width: 1200px;
    height: 970px;
  }
  .business-card {
    position: absolute;
    left: 100px;
    top: 200px;
    width: 1000px;
    height: 571px;
    overflow: hidden;
    background: linear-gradient(135deg, var(--card-light) 0%, var(--card-frost) 55%, var(--card-light) 100%);
    box-shadow: 0 18px 40px rgba(0,0,0,0.18);
  }
  .card-shapes {
    position: absolute;
    inset: 0;
    width: 1000px;
    height: 571px;
  }
  .brand {
    position: absolute;
    left: 55px;
    top: 118px;
    display: flex;
    align-items: center;
    gap: 18px;
    color: var(--brand-blue);
    font-weight: 600;
  }
  .brand-mark {
    width: 34px;
    height: 34px;
    border-radius: 50%;
    background: var(--brand-green);
    flex: none;
  }
  .brand-name {
    font-size: 64px;
    line-height: 1;
    letter-spacing: -0.5px;
  }
  .brand-tagline {
    display: block;
    font-size: 21px;
    letter-spacing: 1.5px;
    margin-top: 10px;
    text-transform: uppercase;
  }
  .contact-block {
    position: absolute;
    right: 47px;
    top: 340px;
    text-align: right;
  }
  .person-name {
    font-size: 35px;
    font-weight: 500;
    line-height: 1.1;
    letter-spacing: 0.5px;
  }
  .person-name .first { color: var(--brand-blue); }
  .person-name .last { color: var(--brand-green); }
  .person-role {
    font-size: 21px;
    font-weight: 300;
    color: var(--muted);
    margin-top: 2px;
  }
  .contact-list {
    list-style: none;
    margin-top: 34px;
  }
  .contact-item {
    display: flex;
    align-items: center;
    justify-content: flex-end;
    gap: 10px;
    font-size: 22px;
    font-weight: 300;
    color: var(--muted);
    height: 33px;
  }
  .contact-item .highlight { color: var(--brand-blue); }
  .contact-icon {
    width: 26px;
    height: 26px;
    flex: none;
  }
</style>
</head>
<body>
<div class="canvas">
  <div class="business-card">
    <svg class="card-shapes" viewBox="0 0 1000 571" aria-hidden="true">
      <defs>
        <linearGradient id="darkPanel" x1="0" y1="0" x2="1" y2="1">
          <stop offset="0" stop-color="var(--card-dark-2)"/>
          <stop offset="1" stop-color="var(--card-dark)"/>
        </linearGradient>
      </defs>
      <path class="accent-band" d="M0,418 C300,425 600,335 795,208 C560,432 300,500 0,522 Z" fill="var(--band-blue)"/>
      <path class="dark-panel" d="M1000,0 C800,255 500,470 0,522 L0,571 L1000,571 Z" fill="url(#darkPanel)"/>
      <path class="silver-edge" d="M1000,0 C800,255 500,470 0,522" fill="none" stroke="var(--silver)" stroke-width="3"/>
    </svg>

    <div class="brand">
      <span class="brand-mark"></span>
      <div class="brand-name">Bright Nest<span class="brand-tagline">Cleaning Service</span></div>
    </div>

    <div class="contact-block">
      <div class="person-name"><span class="first">Liam</span> <span class="last">Carter</span></div>
      <div class="person-role">Managing Partner</div>
      <ul class="contact-list">
        <li class="contact-item">123-555-0148
          <svg class="contact-icon" viewBox="0 0 26 26"><rect x="1" y="1" width="24" height="24" rx="7" fill="var(--brand-green)"/><rect x="8.5" y="5.5" width="9" height="15" rx="1.5" fill="none" stroke="#0b0b0c" stroke-width="2"/></svg>
        </li>
        <li class="contact-item">hello@brightnestclean.com
          <svg class="contact-icon" viewBox="0 0 26 26"><circle cx="13" cy="13" r="12" fill="var(--brand-green)"/><rect x="6.5" y="8.5" width="13" height="9" fill="none" stroke="#0b0b0c" stroke-width="1.6"/><path d="M6.5,8.5 L13,14 L19.5,8.5" fill="none" stroke="#0b0b0c" stroke-width="1.6"/></svg>
        </li>
        <li class="contact-item"><span>www.<span class="highlight">brightnestclean</span>.com</span>
          <svg class="contact-icon" viewBox="0 0 26 26"><circle cx="13" cy="13" r="12" fill="var(--brand-green)"/><circle cx="13" cy="13" r="7" fill="none" stroke="#0b0b0c" stroke-width="1.5"/><ellipse cx="13" cy="13" rx="3" ry="7" fill="none" stroke="#0b0b0c" stroke-width="1.3"/><path d="M6,13 H20" stroke="#0b0b0c" stroke-width="1.3"/></svg>
        </li>
      </ul>
    </div>
  </div>
</div>
</body>
</html>
```